Veltrona Biz Card 2019

New business card for Veltrona Property Inspections. We are a residential home inspection company in Arizona.

Target Market(s)

Real Estate

Font styles to use
Sans Serif

Requirements
Must have
• Glen Marwick
• Home Inspector
• Veltrona Property Inspections, LLC
• 480-555-0173
• glen@veltrona-llc.example

```html
<!DOCTYPE html>
<html lang="en">
<head>
<meta charset="utf-8">
<title>Veltrona Business Card</title>
<link href="https://fonts.googleapis.com/css2?family=Montserrat:wght@400;700&display=swap" rel="stylesheet">
<style>
  :root {
    --backdrop: #161616;
    --card: #232323;
    --card-edge: #2c2c2c;
    --green: #3fb54a;
    --white: #f4f4f4;
    --muted: #bdbdbd;
  }
  html, body {
    margin: 0;
    padding: 0;
    width: 1200px;
    height: 900px;
    overflow: hidden;
    background: var(--backdrop);
    font-family: "Montserrat", sans-serif;
  }
  .canvas {
    position: relative;
    width: 1200px;
    height: 900px;
  }
  .card {
    position: absolute;
    left: 270px;
    width: 660px;
    height: 377px;
    background: linear-gradient(135deg, var(--card) 0%, var(--card-edge) 70%, var(--card) 100%);
    box-shadow: 0 10px 24px rgba(0,0,0,0.55);
    overflow: hidden;
  }
  .card-back { top: 53px; }
  .card-front { top: 470px; }

  .back-mark {
    position: absolute;
    inset: 0;
    display: flex;
    align-items: center;
    justify-content: center;
    gap: 14px;
  }
  .mark-dot {
    width: 20px;
    height: 20px;
    border-radius: 50%;
    background: var(--green);
    flex: none;
  }
  .back-name {
    font-weight: 700;
    font-size: 40px;
    letter-spacing: 3px;
    color: var(--green);
    text-transform: uppercase;
  }

  .brand {
    position: absolute;
    left: 30px;
    top: 0;
    height: 100%;
    width: 270px;
    display: flex;
    align-items: center;
    justify-content: center;
    gap: 12px;
  }
  .brand-name {
    font-weight: 700;
    font-size: 32px;
    letter-spacing: 2px;
    color: var(--white);
    text-transform: uppercase;
  }
  .divider {
    position: absolute;
    left: 318px;
    top: 80px;
    width: 3px;
    height: 220px;
    background: var(--green);
  }
  .contact {
    position: absolute;
    left: 342px;
    top: 82px;
    width: 300px;
    color: var(--white);
  }
  .person-name {
    margin: 0;
    font-weight: 700;
    font-size: 21px;
    color: var(--green);
  }
  .person-role {
    margin: 2px 0 0;
    font-size: 18px;
  }
  .company {
    margin: 4px 0 16px;
    font-size: 13px;
    color: var(--muted);
  }
  .contact-list {
    list-style: none;
    margin: 0;
    padding: 0;
  }
  .contact-list li {
    display: flex;
    align-items: center;
    gap: 10px;
    font-size: 17px;
    line-height: 29px;
    white-space: nowrap;
  }
  .icon {
    width: 15px;
    height: 15px;
    flex: none;
    fill: none;
    stroke: var(--green);
    stroke-width: 2;
  }
  .icon-solid { fill: var(--green); stroke: none; }
</style>
</head>
<body>
<div class="canvas">
  <section class="card card-back">
    <div class="back-mark">
      <span class="mark-dot"></span>
      <span class="back-name">Veltrona</span>
    </div>
  </section>

  <section class="card card-front">
    <div class="brand">
      <span class="mark-dot"></span>
      <span class="brand-name">Veltrona</span>
    </div>
    <div class="divider"></div>
    <div class="contact">
      <p class="person-name">Glen Marwick</p>
      <p class="person-role">Home Inspector</p>
      <p class="company">Veltrona Property Inspections, LLC</p>
      <ul class="contact-list">
        <li>
          <svg class="icon icon-solid" viewBox="0 0 24 24"><path d="M6.6 10.8a15 15 0 0 0 6.6 6.6l2.2-2.2a1 1 0 0 1 1-.25 11.4 11.4 0 0 0 3.6.57 1 1 0 0 1 1 1V20a1 1 0 0 1-1 1A17 17 0 0 1 3 4a1 1 0 0 1 1-1h3.5a1 1 0 0 1 1 1c0 1.25.2 2.45.57 3.57a1 1 0 0 1-.25 1z"/></svg>
          480-555-0173
        </li>
        <li>
          <svg class="icon" viewBox="0 0 24 24"><rect x="3" y="6" width="18" height="12"/><path d="M3 6l9 7 9-7"/></svg>
          glen@veltrona-llc.example
        </li>
        <li>
          <svg class="icon" viewBox="0 0 24 24"><circle cx="12" cy="12" r="9"/><path d="M3 12h18M12 3c3 3 3 15 0 18M12 3c-3 3-3 15 0 18"/></svg>
          www.veltrona-llc.example
        </li>
        <li>
          <svg class="icon icon-solid" viewBox="0 0 24 24"><path d="M12 3l10 9h-3v8h-5v-6h-4v6H5v-8H2z"/></svg>
          Sunvale, AZ 85099, USA
        </li>
      </ul>
    </div>
  </section>
</div>
</body>
</html>
```